Bold, dynamic Brick paver/landscaping company flyer

I need a flyer of 11" long x 8.5" high advertising our brick paver installation service. I want it clean, elegant and bold. I tried to give a general idea of what i was looking for by creating a very poor version for you guys to begin with. That being said, i am no designer, which is why i need your help. You have complete artistic license, show me what you got! I will attach our logo, the photos i used in the mock up as well as the mock up of basic idea. I hate my fonts, i hate to colors of them, i hate the way the pictures overlap without any seperation, but i like the basic idea. Use your artistic vision and skill to transform into something with a flair that will leave my potential customers thinking i am the most upscale service in the area. Please dont hesitate to ask any questions.

all of this bieng said, if you have an awesome idea thats completely different, im not invested in this idea alone, i will consider all options equally. Thanks!

high end homes, wealthy clientle

Advertising

• Must have the blank white box in the upper right corner of approximate size, doesnt have to be exact. the gopher should be removed as well. The text "local postal customer should be there at the bottom of the box.

Company Name, phone number and web address

I like the wording of the text in the upper left, but hate the look of it

```html
<!DOCTYPE html>
<html lang="en">
<head>
<meta charset="utf-8">
<title>Evergrove Landscaping – Paver Flyer</title>
<link rel="stylesheet" href="https://fonts.googleapis.com/css2?family=Dancing+Script:wght@400&family=Mulish:wght@400;600;700&display=swap">
<style>
  :root {
    --page: #e9e9e9;
    --ink: #0a0a0a;
    --cream: #f2eba0;
    --olive: #a7a78c;
    --white: #ffffff;
    --label: #222222;
  }
  * { margin: 0; padding: 0; box-sizing: border-box; }
  html, body {
    width: 1200px; height: 900px; overflow: hidden;
    background: var(--page);
  }
  .flyer {
    position: absolute; left: 50px; top: 25px;
    width: 1100px; height: 850px;
    background: var(--olive);
    overflow: hidden;
  }
  .photo { position: absolute; }
  .photo--firepit {
    left: 0; top: 0; width: 329px; height: 164px;
    background: linear-gradient(170deg, #1d2a1c 0%, #3b4a2a 35%, #5a4b3a 65%, #2e2824 100%);
  }
  .photo--patio {
    left: 341px; top: 0; width: 323px; height: 164px;
    background: linear-gradient(175deg, #1e211c 0%, #4d4235 30%, #8a7561 60%, #a89380 100%);
  }
  .photo--home {
    left: 0; top: 183px; width: 664px; height: 470px;
    background: linear-gradient(180deg, #5f86b8 0%, #37527a 30%, #3c4a3a 55%, #6f6a64 72%, #9b958d 100%);
  }
  .mail-box {
    position: absolute; left: 664px; top: 0; width: 436px; height: 183px;
    background: var(--white);
  }
  .mail-box__label {
    position: absolute; left: 0; right: 0; bottom: 14px;
    text-align: center;
    font: 400 22px/1 "Mulish", sans-serif;
    color: var(--label);
  }
  .tagline-panel {
    position: absolute; left: 664px; top: 183px; width: 436px; height: 520px;
    background: var(--ink);
  }
  .tagline {
    position: absolute; left: 0; right: 0;
    text-align: center;
    font: 400 54px/60px "Dancing Script", cursive;
    color: var(--cream);
  }
  .tagline--first { top: 30px; }
  .tagline--second { top: 270px; }
  .wave { position: absolute; left: 0; top: 575px; width: 1100px; height: 275px; }
  .brand {
    position: absolute; left: 0; right: 0; top: 650px;
    text-align: center;
    font: 400 78px/1 "Dancing Script", cursive;
    color: var(--cream);
    padding-left: 40px;
  }
  .contact {
    position: absolute; left: 0; right: 0; text-align: center;
    color: var(--cream); font-family: "Mulish", sans-serif;
  }
  .contact--web { top: 748px; font-size: 27px; font-weight: 400; }
  .contact--web b { font-weight: 700; }
  .contact--phone { top: 790px; font-size: 28px; font-weight: 600; letter-spacing: 1px; }
</style>
</head>
<body>
  <main class="flyer">
    <div class="photo photo--firepit" role="img" aria-label="Evening patio with fire pit and lounge chairs"></div>
    <div class="photo photo--patio" role="img" aria-label="Paver patio with outdoor fireplace and dining set"></div>
    <div class="photo photo--home" role="img" aria-label="Modern home at dusk with lit paver driveway and garden"></div>

    <div class="mail-box">
      <p class="mail-box__label">local postal customer</p>
    </div>

    <section class="tagline-panel">
      <p class="tagline tagline--first">Where the<br>elegance of<br>pavers</p>
      <p class="tagline tagline--second">Meets the<br>beauty of design</p>
    </section>

    <svg class="wave" viewBox="0 0 1100 275" preserveAspectRatio="none" aria-hidden="true">
      <path d="M0 32 C 260 10, 560 8, 1100 40 L1100 56 C 560 26, 260 30, 0 58 Z" fill="#a7a78c"/>
      <path d="M0 58 C 260 30, 560 26, 1100 56 L1100 275 L0 275 Z" fill="#0a0a0a"/>
    </svg>

    <h1 class="brand">Evergrove Landscaping</h1>
    <p class="contact contact--web">www.<b>evergrove</b>landscaping.com</p>
    <p class="contact contact--phone">(757) 555-0148</p>
  </main>
</body>
</html>
```